Carvo Group Business Card

Building Management company based in Sydney, Australia. We provide onsite management for commercial and residential buildings.
I would like a sophisticated minimalist design that indicates that we provide a high-end service. I would like a silver or metal look background or something similar.
The business card should have:
Name
Title
email
Office Phone
Mobile
Address
Website
The services that we provide should be prominent:
Building Management - Concierge - Caretaking - Cleaning

```html
<!DOCTYPE html>
<html lang="en">
<head>
<meta charset="utf-8">
<title>Carvo Group Business Card</title>
<link rel="stylesheet" href="https://fonts.googleapis.com/css2?family=Open+Sans:wght@400;600;700&display=swap">
<style>
  :root {
    --silver-light: #c9cbce;
    --silver-mid: #a7a9ad;
    --silver-dark: #8c8e92;
    --card-black: #050505;
    --card-sheen: #2a2b2d;
    --strip-dark: #151515;
    --brand-blue: #1a6ab3;
    --text-white: #ffffff;
    --text-soft: #e6e6e6;
    --text-silver: #b9bcc0;
  }
  * { box-sizing: border-box; margin: 0; padding: 0; }
  html, body { width: 1200px; height: 900px; overflow: hidden; }
  body {
    background: linear-gradient(135deg, var(--silver-light) 0%, var(--silver-mid) 45%, var(--silver-light) 65%, var(--silver-dark) 100%);
    font-family: "Open Sans", Arial, sans-serif;
    display: flex;
    flex-direction: column;
    align-items: center;
    justify-content: center;
    gap: 56px;
  }
  .card {
    position: relative;
    width: 660px;
    height: 377px;
    background:
      linear-gradient(120deg, transparent 0%, rgba(255,255,255,0.07) 38%, transparent 52%, rgba(255,255,255,0.04) 78%, transparent 100%),
      linear-gradient(180deg, var(--card-sheen) 0%, var(--card-black) 40%, var(--card-black) 100%);
    overflow: hidden;
    box-shadow: 0 6px 18px rgba(0,0,0,0.35);
  }
  .card__rule {
    position: absolute;
    left: 0; right: 0;
    height: 8px;
    background: linear-gradient(90deg, #d8dadd, #ffffff 50%, #d8dadd);
  }
  .card__band {
    position: absolute;
    left: 0; right: 0; bottom: 0;
    background: var(--brand-blue);
  }
  .wordmark {
    display: flex;
    align-items: center;
    gap: 10px;
    color: var(--text-white);
    font-weight: 700;
    letter-spacing: 1px;
    text-transform: uppercase;
    white-space: nowrap;
  }
  .wordmark__square {
    width: 18px; height: 18px;
    background: var(--brand-blue);
  }
  .services {
    color: var(--text-silver);
    font-size: 12px;
    font-weight: 600;
    letter-spacing: 2px;
    text-transform: uppercase;
    white-space: nowrap;
  }

  /* front */
  .front-brand {
    position: absolute;
    left: 0; right: 0; top: 112px;
    display: flex;
    flex-direction: column;
    align-items: center;
    gap: 18px;
  }
  .card--front .wordmark { font-size: 34px; }
  .card--front .card__rule { bottom: 60px; }
  .card--front .card__band { height: 52px; }

  /* back */
  .card--back .wordmark {
    position: absolute;
    left: 34px; top: 108px;
    font-size: 26px;
  }
  .person {
    position: absolute;
    right: 30px; top: 40px;
    text-align: right;
  }
  .person__name {
    color: var(--brand-blue);
    font-weight: 600;
    font-size: 21px;
    letter-spacing: 1px;
    text-transform: uppercase;
  }
  .person__title {
    color: var(--text-white);
    font-size: 15px;
    margin-top: 2px;
  }
  .contact-strip {
    position: absolute;
    left: 0; right: 0;
    top: 168px; height: 140px;
    background: var(--strip-dark);
    display: grid;
    grid-template-columns: 1.25fr 1fr 1.1fr;
    align-items: center;
    padding: 0 28px;
    color: var(--text-soft);
    font-size: 14px;
  }
  .contact-group { display: flex; flex-direction: column; gap: 8px; }
  .contact-line { display: flex; align-items: flex-start; gap: 7px; line-height: 1.5; }
  .contact-line svg { flex: none; width: 13px; height: 13px; margin-top: 4px; fill: var(--brand-blue); }
  .card--back .card__rule { bottom: 62px; }
  .card--back .card__band {
    height: 54px;
    display: flex;
    align-items: center;
    justify-content: center;
  }
  .card--back .services { color: var(--text-white); font-size: 11px; }
</style>
</head>
<body>

<section class="card card--front" aria-label="Card front">
  <div class="front-brand">
    <div class="wordmark"><span class="wordmark__square"></span>Carvo Group</div>
    <p class="services">Building Management · Concierge · Caretaking · Cleaning</p>
  </div>
  <div class="card__rule"></div>
  <div class="card__band"></div>
</section>

<section class="card card--back" aria-label="Card back">
  <div class="wordmark"><span class="wordmark__square"></span>Carvo Group</div>
  <div class="person">
    <p class="person__name">Daniel Reyes</p>
    <p class="person__title">Managing Director</p>
  </div>
  <div class="contact-strip">
    <div class="contact-group">
      <p class="contact-line">
        <svg viewBox="0 0 12 12"><path d="M6 0a4 4 0 0 0-4 4c0 3 4 8 4 8s4-5 4-8a4 4 0 0 0-4-4zm0 5.6A1.6 1.6 0 1 1 6 2.4a1.6 1.6 0 0 1 0 3.2z"/></svg>
        <span>1234, Address Goes Here,<br>Country Name, 123456</span>
      </p>
    </div>
    <div class="contact-group">
      <p class="contact-line">
        <svg viewBox="0 0 12 12"><path d="M1 4c0-2 2-3 5-3s5 1 5 3H8V3H4v1zM2 5h8l1 6H1zm4 1.5a1.5 1.5 0 1 0 0 3 1.5 1.5 0 0 0 0-3z"/></svg>
        <span>123.456.7890</span>
      </p>
      <p class="contact-line">
        <svg viewBox="0 0 12 12"><path d="M3 0h6a1 1 0 0 1 1 1v10a1 1 0 0 1-1 1H3a1 1 0 0 1-1-1V1a1 1 0 0 1 1-1zm0 2v7h6V2zm3 8a.6.6 0 1 0 0 1.2A.6.6 0 0 0 6 10z"/></svg>
        <span>123.456.7890</span>
      </p>
    </div>
    <div class="contact-group">
      <p class="contact-line">
        <svg viewBox="0 0 12 12"><path d="M0 2h12v8H0zm1 1v.3l5 3.4 5-3.4V3zm0 1.6V9h10V4.6L6 8z"/></svg>
        <span>info@youremail.com</span>
      </p>
      <p class="contact-line">
        <svg viewBox="0 0 12 12"><path d="M5 7 7 5l1 1-2 2zM3 6 1.5 7.5a2 2 0 0 0 3 3L6 9 5 8 3.5 9.5a.7.7 0 0 1-1-1L4 7zm6 0 1.5-1.5a2 2 0 0 0-3-3L6 3l1 1 1.5-1.5a.7.7 0 0 1 1 1L8 5z"/></svg>
        <span>www.website.com</span>
      </p>
    </div>
  </div>
  <div class="card__rule"></div>
  <div class="card__band">
    <p class="services">Building Management · Concierge · Caretaking · Cleaning</p>
  </div>
</section>

</body>
</html>
```